Veterinary Pylon

My veterinary clinic is not clearly visible from the street and I want to place a Pylon next to my driveway. I want a modern, elegant straight Design, the Photo shows the sheduled place. One can see the clinic on our Homepage: www.fernhollow-tierpraxis.at
The last pictures are examples for pylones I like

Target Market(s)

the passing cars often miss my entry...I want to show where to turn left

Colors
3276b5
33a6d7
00a990

Requirements
Must have
• High value, simple elegance, size: 250cm (high) x 100cm (width)
Nice to have
• Our Logo, arrow(?)

A special Text is not necessary but this will be an option:

Biegen sie hier ab und wir biegen es wieder hin!
Should not have
• Too much Color, the colors I have chosen are the possible colors but it‘s not necessary to use them.

```html
<!DOCTYPE html>
<html lang="de">
<head>
<meta charset="utf-8">
<title>Fernhollow Tierpraxis – Pylon</title>
<link rel="stylesheet" href="https://fonts.googleapis.com/css2?family=Josefin+Sans:wght@400;600;700&display=swap">
<style>
  :root {
    --backdrop: #eeeeee;
    --panel: #ffffff;
    --navy: #2b4a97;
    --sky: #33a6d7;
    --sky-soft: #5fc0e2;
    --arrow: #ffffff;
  }
  * { margin: 0; padding: 0; box-sizing: border-box; }
  html, body {
    width: 1200px;
    height: 1001px;
    overflow: hidden;
    background: var(--backdrop);
  }
  .canvas {
    position: relative;
    width: 1200px;
    height: 1001px;
  }
  .pylon-face {
    position: absolute;
    left: 420px;
    top: 50px;
    width: 360px;
    height: 900px;
    background: var(--panel);
    overflow: hidden;
    font-family: "Josefin Sans", sans-serif;
  }
  .brand {
    position: absolute;
    top: 44px;
    left: 0;
    width: 100%;
    text-align: center;
    color: var(--navy);
    font-weight: 700;
  }
  .brand-dot {
    display: block;
    width: 70px;
    height: 70px;
    margin: 0 auto 26px;
    border-radius: 50%;
    background: var(--navy);
  }
  .brand-name {
    display: block;
    font-size: 40px;
    line-height: 1;
    letter-spacing: 1px;
  }
  .brand-sub {
    display: block;
    margin-top: 8px;
    font-size: 19px;
    letter-spacing: 4px;
    text-transform: uppercase;
  }
  .direction {
    position: absolute;
    left: 0;
    top: 250px;
    width: 360px;
    height: 110px;
  }
  .tagline {
    position: absolute;
    left: 42px;
    top: 418px;
    font-size: 22px;
    line-height: 1.32;
    font-weight: 600;
    color: var(--sky);
  }
  .hours {
    position: absolute;
    left: 44px;
    top: 508px;
    color: var(--navy);
    font-weight: 400;
  }
  .hours-title {
    font-size: 10.5px;
    letter-spacing: 2px;
    text-transform: uppercase;
    color: var(--sky);
    margin-bottom: 10px;
  }
  .hours-day {
    font-size: 9.5px;
    letter-spacing: .6px;
    text-transform: uppercase;
    line-height: 14px;
  }
  .hours-time {
    font-size: 9.5px;
    letter-spacing: .4px;
    line-height: 14px;
    margin-bottom: 12px;
  }
</style>
</head>
<body>
<main class="canvas">
  <section class="pylon-face" aria-label="Pylon Vorderseite">
    <header class="brand">
      <span class="brand-dot"></span>
      <span class="brand-name">Fernhollow</span>
      <span class="brand-sub">Tierpraxis</span>
    </header>

    <svg class="direction" viewBox="0 0 360 110" aria-label="Pfeil nach links">
      <rect x="0" y="50" width="252" height="10" fill="var(--navy)"/>
      <circle cx="311" cy="55" r="51" fill="var(--sky-soft)"/>
      <line x1="282" y1="55" x2="338" y2="55" stroke="var(--arrow)" stroke-width="6" stroke-linecap="round"/>
      <polyline points="300,39 282,55 300,71" fill="none" stroke="var(--arrow)" stroke-width="6" stroke-linecap="round" stroke-linejoin="round"/>
    </svg>

    <p class="tagline">Biegen Sie Hier Ab Und Wir<br>Biegen Es Wieder Hin!</p>

    <div class="hours">
      <p class="hours-title">Unsere Ordinationszeiten:</p>
      <p class="hours-day">Montag bis Freitag :</p>
      <p class="hours-time">8:00–12:00 UND 14:00–19:00</p>
      <p class="hours-day">Samstag :</p>
      <p class="hours-time">8:00–12:00 UND 17:00–18:00</p>
      <p class="hours-day">Sonntag :</p>
      <p class="hours-time">10:00–11:00 UND 17:00–18:00</p>
    </div>
  </section>
</main>
</body>
</html>
```